QRV designs

qrv designs is an interior design firm in omaha, NE. Offering complete residential/commercial design. Exterior, int finishes, cabinets, furniture, window covering. Have been in business for 25 yrs. Lived in and/or completed work in LA, NYC, PHX, MIami, London, Canada, Mexico. We would like to see a marketing flyer with clean, architectural design. Modern .Flyer will be on display at open houses & mailed to perspective clients. Dont want a lot of color. Prefer whites/black, greys or brown. Maybe small accent of blue like logo. Block architectural lettering. do not need to use all photos. but use at least one from each of the three projects. thanks for you time
Updates

please change/add on any and all submissions the following add: Dana Whitcombe, Principal (in info section not on logo) change: Info@qrvdesigns.com, not dana @qrvdesigns.com add: back design, would like to use as many photos as possible thanks you

Industry/Entity Type

Residential

```html
<!DOCTYPE html>
<html lang="en">
<head>
<meta charset="utf-8">
<title>QRV designs – Flyer</title>
<link href="https://fonts.googleapis.com/css2?family=Delius&family=Open+Sans:wght@400&display=swap" rel="stylesheet">
<style>
  :root {
    --paper: #ffffff;
    --frame: #000000;
    --brown: #4a3324;
    --blue: #1f6fbf;
    --text-light: #f3ede6;
    --photo-dark: #1d1a18;
    --photo-mid: #4e4740;
    --photo-warm: #7a6a5a;
  }
  * { margin: 0; padding: 0; box-sizing: border-box; }
  html, body { width: 822px; height: 1200px; overflow: hidden; background: var(--paper); }
  .flyer { position: relative; width: 822px; height: 1200px; background: var(--paper); }
  .frame {
    position: absolute; left: 60px; top: 89px; width: 678px; height: 1048px;
    background: var(--frame);
  }
  .hero-photo {
    position: absolute; left: 81px; top: 121px; width: 639px; height: 590px;
    background:
      radial-gradient(ellipse at 40% 65%, rgba(180,120,60,0.35), transparent 30%),
      linear-gradient(180deg, var(--photo-mid) 0%, var(--photo-dark) 45%, var(--photo-warm) 62%, var(--photo-dark) 100%);
  }
  .brand-box {
    position: absolute; left: 81px; top: 121px; width: 257px; height: 201px;
    background: var(--brown);
    display: flex; align-items: center; justify-content: center;
  }
  .brand-name {
    font-family: "Delius", cursive;
    font-size: 42px; color: var(--text-light); text-align: center; line-height: 1.15;
  }
  .wave { position: absolute; left: 81px; top: 660px; width: 639px; height: 60px; }
  .info-panel {
    position: absolute; left: 81px; top: 718px; width: 639px; height: 350px;
    background: var(--brown);
    padding: 26px 40px 0 63px;
    font-family: "Delius", cursive;
    color: var(--text-light);
    font-size: 20px; line-height: 29px; letter-spacing: 0.2px;
  }
  .info-panel p + p { margin-top: 8px; }
  .accent-rule { position: absolute; left: 81px; top: 1068px; width: 639px; height: 8px; background: var(--blue); }
  .contact {
    position: absolute; left: 107px; right: 106px; top: 1090px;
    display: flex; justify-content: space-between;
    font-family: "Open Sans", Arial, sans-serif; font-size: 19px; color: var(--paper);
  }
</style>
</head>
<body>
<div class="flyer">
  <div class="frame"></div>
  <div class="hero-photo" role="img" aria-label="Photo of a modern open-plan kitchen and living room with vaulted timber-beamed ceiling, fireplace and stone island"></div>
  <div class="brand-box">
    <div class="brand-name">QRV designs</div>
  </div>
  <svg class="wave" viewBox="0 0 639 60" preserveAspectRatio="none" aria-hidden="true">
    <path d="M0 40 C 150 8, 300 10, 420 30 C 520 44, 590 30, 639 10 L639 60 L0 60 Z" fill="var(--blue)"/>
    <path d="M0 50 C 150 22, 300 22, 420 40 C 520 54, 590 40, 639 22 L639 60 L0 60 Z" fill="var(--brown)"/>
  </svg>
  <section class="info-panel">
    <p>qrv designs has offered complete design services for residential and commercial projects for over 25 years. Our diversity has allowed QRV designs to design new construction and renovation projects in New York, California, Florida, Arizona and Mexico.</p>
    <p>We can work with your builder to coordinate the many architectural details required to create your personal space. Thus allowing your project to progress smoothly and more cost effectively.</p>
    <p>please call to talk about your upcoming project.</p>
  </section>
  <div class="accent-rule"></div>
  <footer class="contact">
    <span>Phone : 402-555-0148</span>
    <span>Info@qrvdesigns.com</span>
  </footer>
</div>
</body>
</html>
```